I need a new business card design for my pharmacy.

I need a business card design. I will include my logo.
The card needs to be readable. I prefer to have my logo on one side along with my website, the other side includes the other information. Please use combination of black, neon green, white, and silver. This needs to catch the eye but yet be clearly visible and legible. Thanks

Industry/Entity Type

Pharmacy

Contact Information for Business Card

It needs to have the following information listed:
Mel's Apothecary Owner/Pharm D.
7134 North Brook Lane
Sioux Falls, SD 57231
Phone 605-318-6207
Fax 605-318-6209
email: mel@melsapothecary-example.com
www.melsapothecary-example.com
Store hours Monday-Friday 8 am- 7 pm
Saturday 8 am- 12 pm
Sunday Closed
Please utilize the colors black, white, and neon green, maybe silver.

Requirements
Must have
• It needs to be easily readable!
Nice to have
• It should catch the eye.
Should not have
• Do not use any other colors except listed: black, neon green, white, & silver.

```html
<!DOCTYPE html>
<html lang="en">
<head>
<meta charset="utf-8">
<title>Mel's Apothecary – Business Card</title>
<link rel="stylesheet" href="https://fonts.googleapis.com/css2?family=Ubuntu:wght@400;500;700&display=swap">
<style>
  :root {
    --ink: #1f1c1a;
    --paper: #ffffff;
    --neon: #a7c93c;
    --silver: #c9c9c9;
  }
  html, body {
    margin: 0;
    padding: 0;
    width: 937px;
    height: 1200px;
    overflow: hidden;
    background: var(--paper);
    font-family: "Ubuntu", sans-serif;
  }
  .canvas {
    position: relative;
    width: 937px;
    height: 1200px;
  }
  .card-front {
    position: absolute;
    left: 2px;
    top: 0;
    width: 932px;
    height: 573px;
    background: var(--ink);
    color: var(--paper);
    border: 1px solid #555;
    box-sizing: border-box;
  }
  .front-brand {
    position: absolute;
    left: 0;
    right: 0;
    top: 300px;
    text-align: center;
    font-size: 62px;
    font-weight: 700;
    letter-spacing: -1.5px;
  }
  .front-web {
    position: absolute;
    left: 0;
    right: 0;
    top: 492px;
    text-align: center;
    font-size: 27px;
    font-weight: 400;
  }
  .card-back {
    position: absolute;
    left: 0;
    top: 620px;
    width: 935px;
    height: 580px;
    background: var(--paper);
    border: 1px solid var(--silver);
    box-sizing: border-box;
    color: var(--ink);
  }
  .back-brand {
    position: absolute;
    left: 62px;
    top: 60px;
    font-size: 52px;
    font-weight: 700;
    letter-spacing: -1.5px;
  }
  .holder-name {
    position: absolute;
    left: 61px;
    top: 232px;
    font-size: 37px;
    font-weight: 500;
  }
  .holder-title {
    position: absolute;
    left: 61px;
    top: 285px;
    font-size: 24px;
    font-weight: 500;
  }
  .rule {
    position: absolute;
    left: 61px;
    top: 319px;
    width: 832px;
    height: 2px;
    background: var(--neon);
  }
  .contact, .address {
    position: absolute;
    top: 369px;
    font-size: 23px;
    line-height: 35px;
  }
  .contact { left: 61px; }
  .address { left: 624px; }
  .hours-band {
    position: absolute;
    left: 0;
    bottom: 0;
    width: 935px;
    height: 60px;
  }
  .hours-band svg { position: absolute; inset: 0; }
  .hours {
    position: absolute;
    top: 0;
    height: 60px;
    line-height: 62px;
    font-size: 23px;
    white-space: nowrap;
  }
  .hours-week { left: 21px; color: var(--ink); }
  .hours-sat { left: 485px; color: var(--paper); }
  .hours-sun { left: 767px; color: var(--ink); }
</style>
</head>
<body>
<div class="canvas">
  <section class="card-front">
    <div class="front-brand">Mel's Apothecary</div>
    <div class="front-web">www.melsapothecary-example.com</div>
  </section>

  <section class="card-back">
    <div class="back-brand">Mel's Apothecary</div>

    <div class="holder-name">Mel's Apothecary</div>
    <div class="holder-title">Owner/Pharm D.</div>
    <div class="rule"></div>

    <div class="contact">
      Phone 605-318-6207<br>
      Fax 605-318-6209<br>
      mel@melsapothecary-example.com
    </div>
    <div class="address">
      7134 North Brook Lane<br>
      Sioux Falls, SD 57231
    </div>

    <div class="hours-band">
      <svg width="935" height="60" viewBox="0 0 935 60" aria-hidden="true">
        <rect x="0" y="0" width="935" height="60" fill="var(--neon)"/>
        <polygon points="478,0 753,0 727,60 451,60" fill="var(--ink)"/>
        <polygon points="473,0 478,0 451,60 446,60" fill="var(--paper)"/>
        <polygon points="753,0 758,0 732,60 727,60" fill="var(--paper)"/>
      </svg>
      <span class="hours hours-week">Store hours Monday-Friday 8 am- 7 pm</span>
      <span class="hours hours-sat">Saturday 8 am- 12 pm</span>
      <span class="hours hours-sun">Sunday Closed</span>
    </div>
  </section>
</div>
</body>
</html>
```